Wild Mo's Wine Label Project

We need a new entry level wine label called "Wild Mo's" for a range of wines we are developing from inland Australia. Our company is made up of three youngish guys who live hard and love taking the mickey. Wild Mo is Wild Moss - the largest and loudest of the three partners (and ideally this label will take the mickey out of him). We've grown the grapes ourselves for this first release which will be a 2012 Pinot Gris. Wine style is dry, young, fresh and contemporary and pitched at the sub AUD $10 retail price point. The package will be flint (clear) claret shape bottle with plain screwcap (colour matched to suit the winning label design).

I've attached a couple of photos of Wild Moss to give you some idea of his presence and persona.

Target Market(s)

Semi educated 25 - 40 year old wine drinkers. Skewed towards females.

Industry/Entity Type

Retail

Requirements
Should not have
• Anything traditional or old fashioned

```html
<!DOCTYPE html>
<html lang="en">
<head>
<meta charset="utf-8">
<title>Wild Mo's 2012 Pinot Gris Label</title>
<link rel="stylesheet" href="https://fonts.googleapis.com/css2?family=Risque&family=Smokum&family=Federo&family=Arimo:wght@700&display=swap">
<style>
  :root {
    --label-black: #000000;
    --cream: #f6e7b4;
    --title-ink: #0d0b08;
    --title-halo: #fffbe6;
    --art-peach: #f3c48a;
    --art-orange: #e9936a;
    --art-yellow: #f6d545;
    --art-pale: #f8e7a8;
  }
  * { margin: 0; padding: 0; box-sizing: border-box; }
  html, body {
    width: 733px;
    height: 1200px;
    overflow: hidden;
    background: var(--label-black);
  }
  .label {
    position: relative;
    width: 733px;
    height: 1200px;
    background: var(--label-black);
    color: var(--cream);
  }
  .winery-name {
    position: absolute;
    top: 48px;
    left: 0;
    width: 100%;
    text-align: center;
    font-family: "Risque", cursive;
    font-weight: 400;
    font-size: 40px;
    letter-spacing: 1px;
    text-transform: uppercase;
    line-height: 1;
    white-space: nowrap;
  }
  .artwork {
    position: absolute;
    left: 77px;
    top: 152px;
    width: 575px;
    height: 698px;
    overflow: hidden;
    background:
      radial-gradient(ellipse 60% 40% at 55% 38%, var(--art-orange) 0%, rgba(233,147,106,0) 70%),
      radial-gradient(ellipse 80% 35% at 35% 80%, var(--art-yellow) 0%, rgba(246,213,69,0) 75%),
      linear-gradient(160deg, var(--art-pale) 0%, var(--art-peach) 40%, var(--art-orange) 60%, var(--art-yellow) 85%, var(--art-pale) 100%);
  }
  .wine-name {
    position: absolute;
    top: 640px;
    left: 77px;
    width: 575px;
    text-align: center;
    font-family: "Smokum", serif;
    font-weight: 400;
    font-size: 100px;
    line-height: 1;
    letter-spacing: 3px;
    text-transform: uppercase;
    white-space: nowrap;
    color: var(--title-ink);
    text-shadow: 5px 3px 0 var(--title-halo), 7px 5px 0 var(--title-halo);
  }
  .vintage {
    position: absolute;
    top: 893px;
    left: 0;
    width: 100%;
    text-align: center;
    font-family: "Federo", sans-serif;
    font-size: 82px;
    line-height: 1;
  }
  .variety {
    position: absolute;
    top: 1010px;
    left: 0;
    width: 100%;
    text-align: center;
    font-family: "Risque", cursive;
    font-size: 56px;
    line-height: 1;
    letter-spacing: 1px;
    text-transform: uppercase;
    white-space: nowrap;
  }
  .statutory {
    position: absolute;
    top: 1152px;
    left: 52px;
    right: 55px;
    display: flex;
    justify-content: space-between;
    font-family: "Arimo", sans-serif;
    font-weight: 700;
    font-size: 23px;
    line-height: 1;
  }
</style>
</head>
<body>
  <main class="label">
    <h2 class="winery-name">Scarlet Thursday Winery</h2>
    <div class="artwork" role="img" aria-label="Abstract painting of a dark palm tree sweeping over a warm orange and yellow desert sky"></div>
    <h1 class="wine-name">Wild Mo's</h1>
    <p class="vintage">2012</p>
    <p class="variety">Pinot Gris</p>
    <footer class="statutory">
      <span class="alcohol">ALC. 12%</span>
      <span class="origin">AUSTRALIA</span>
      <span class="volume">750 mL</span>
    </footer>
  </main>
</body>
</html>
```